Legal Service Estimated Retainer and Average Case Value

We need an 11x14 flyer that contains the standard retainers and average cost be case, both provided in documents, for each case type we handle. We need the information displayed, preferably in a way that makes the information readable but less troubling to a client shocked at price of litigation. We need one sheet with the retainers and average case value merged into one table.

Target Market(s)

Potential Clients

Font styles to use
Serif
Sans Serif

```html
<!DOCTYPE html>
<html lang="en">
<head>
<meta charset="utf-8">
<title>Retainer and Average Fee per Case Type</title>
<link href="https://fonts.googleapis.com/css2?family=Cinzel:wght@500&family=Montserrat:wght@700;800&family=Roboto:wght@400;500&display=swap" rel="stylesheet">
<style>
  :root {
    --navy: #23264f;
    --paper: #f6f6f6;
    --backdrop: #e3e3e3;
    --ink: #3a3a3a;
    --rule: #6b6b6b;
    --white: #ffffff;
    --photo-dark: #3b2a1e;
    --photo-warm: #9a5a2c;
    --photo-light: #c9ccd0;
  }
  * { box-sizing: border-box; margin: 0; padding: 0; }
  html, body { width: 1200px; height: 864px; overflow: hidden; }
  body { background: var(--backdrop); font-family: "Roboto", Arial, sans-serif; color: var(--ink); }

  .flyer {
    position: absolute; left: 270px; top: 12px;
    width: 660px; height: 840px;
    background: var(--paper);
    box-shadow: 0 6px 18px rgba(0,0,0,.12);
    overflow: hidden;
  }

  .hero-photo {
    position: absolute; left: 0; top: 40px; width: 300px; height: 212px;
    background: linear-gradient(160deg, var(--photo-light) 0%, #8c857c 35%, var(--photo-warm) 65%, var(--photo-dark) 100%);
  }

  .firm-name {
    position: absolute; left: 322px; top: 44px;
    display: flex; align-items: center; gap: 10px;
    font-family: "Cinzel", Georgia, serif; font-weight: 500; color: var(--navy);
  }
  .firm-name .mark { width: 34px; height: 34px; background: var(--navy); }
  .firm-name .lines { line-height: 1.05; }
  .firm-name .small { font-size: 10px; letter-spacing: .5px; }
  .firm-name .big { font-size: 22px; letter-spacing: .5px; }

  .intro {
    position: absolute; left: 322px; top: 104px; width: 318px;
    font-size: 12.5px; line-height: 1.55; color: var(--ink);
  }

  .title-band {
    position: absolute; left: 0; top: 262px; width: 612px; height: 34px;
    background: var(--navy);
    clip-path: polygon(0 0, 100% 0, 100% 100%, 0 100%);
    display: flex; align-items: center; padding-left: 70px;
    color: var(--white); font-family: "Montserrat", Arial, sans-serif; font-weight: 800;
    font-size: 15px; letter-spacing: 4px;
  }
  .title-band .slant { position: absolute; left: 0; top: 0; }

  .fee-table {
    position: absolute; left: 26px; top: 300px; width: 610px;
    border-collapse: collapse; font-size: 12px;
  }
  .fee-table th {
    background: var(--navy); color: var(--white); height: 30px;
    font-family: "Montserrat", Arial, sans-serif; font-weight: 700; font-size: 12px; letter-spacing: 2px;
    text-align: center;
  }
  .fee-table th.case-col { text-align: left; padding-left: 70px; }
  .fee-table td {
    height: 32px; border: 1px solid var(--rule); padding: 0 8px;
    background: var(--paper); font-weight: 500;
  }
  .fee-table td.case { width: 300px; }
  .fee-table td.retainer, .fee-table td.fee { text-align: center; }
  .fee-table td.retainer { width: 140px; }

  .footer-band {
    position: absolute; left: 0; bottom: 0; width: 660px; height: 70px;
    background: var(--navy); color: var(--white);
  }
  .footer-band .divider { position: absolute; left: 0; top: 0; }
  .footer-band .web {
    position: absolute; left: 34px; top: 24px;
    font-family: "Montserrat", Arial, sans-serif; font-weight: 700; font-size: 17px;
  }
  .footer-band .contact {
    position: absolute; right: 26px; top: 14px; text-align: left;
    font-family: "Montserrat", Arial, sans-serif; font-weight: 700; font-size: 14px; line-height: 1.3;
  }
  .footer-band .contact strong { font-size: 17px; }
</style>
</head>
<body>
<main class="flyer">
  <div class="hero-photo" role="img" aria-label="Wooden gavel resting on a courtroom bench"></div>

  <div class="firm-name">
    <span class="mark"></span>
    <div class="lines">
      <div class="small">THE LAW OFFICE OF</div>
      <div class="big">MORGAN T ELLSWORTH</div>
    </div>
  </div>

  <p class="intro">In order for our clients to set expectations for legal fees, we provide the national average range of fees and retainer per case type. These are only to provide you with an understanding of what other cases have cost clients in similar cases. Please note these are not estimates nor guarantees of your own legal costs.</p>

  <div class="title-band">
    <svg class="slant" width="22" height="34" aria-hidden="true"><polygon points="0,0 22,0 0,34" fill="var(--paper)"/></svg>
    RETAINER AND AVERAGE FEE PER CASE TYPE
  </div>

  <table class="fee-table">
    <thead>
      <tr><th class="case-col">CASE TYPE</th><th>RETAINERS</th><th>AVERAGE FEE</th></tr>
    </thead>
    <tbody>
      <tr><td class="case">Divorce (3301 C)</td><td class="retainer">$ 2,000</td><td class="fee">$ 1,500 - $ 3,000</td></tr>
      <tr><td class="case">Divorce (3301 D)</td><td class="retainer">$ 2,500</td><td class="fee">$ 2,000 - $ 3,000</td></tr>
      <tr><td class="case">Divorce &amp; Custody</td><td class="retainer">$ 3,500</td><td class="fee">$ 5,000 - $ 8,000</td></tr>
      <tr><td class="case">Divorce &amp; Equitable Distribution</td><td class="retainer">$ 3,500</td><td class="fee">$ 6,000 - $ 10,000</td></tr>
      <tr><td class="case">Divorce &amp; Support</td><td class="retainer">$ 3,000</td><td class="fee">$ 2,000 - $ 4,000</td></tr>
      <tr><td class="case">Divorce, Custody &amp; Support</td><td class="retainer">$ 3,500</td><td class="fee">$ 8,000 - $ 12,000</td></tr>
      <tr><td class="case">Divorce, Equitable Distribution and Support</td><td class="retainer">$ 3,500</td><td class="fee">$ 10,000 - $ 12,000</td></tr>
      <tr><td class="case">Divorce, Equitable Distribution and Custody</td><td class="retainer">$ 5,000</td><td class="fee">$ 10,000 - $ 15,000</td></tr>
      <tr><td class="case">Divorce, Equitable Distribution, Custody and Support</td><td class="retainer">$ 3,500</td><td class="fee">$ 2,000 - $ 15,000</td></tr>
      <tr><td class="case">Custody Initial Order</td><td class="retainer">$ 3,000</td><td class="fee">$ 4,000 - $ 7,000</td></tr>
      <tr><td class="case">Custody Modification</td><td class="retainer">$ 3,500</td><td class="fee">$ 5,000 - $ 8,000</td></tr>
      <tr><td class="case">Custody and Support</td><td class="retainer">$ 3,000</td><td class="fee">$ 5,000 - $ 8,000</td></tr>
      <tr><td class="case">(PFA) Protection From Abuse</td><td class="retainer">$2,000 Paid In Full</td><td class="fee">$ 1,500 - $ 3,000</td></tr>
    </tbody>
  </table>

  <footer class="footer-band">
    <svg class="divider" width="660" height="70" aria-hidden="true">
      <polygon points="0,0 420,0 420,0 0,0" fill="none"/>
      <line x1="448" y1="0" x2="470" y2="70" stroke="var(--white)" stroke-width="3"/>
    </svg>
    <div class="web">https://www.ellsworthfamilylaw.com</div>
    <div class="contact">Contact info :<br><strong>(555) 214-0736</strong></div>
  </footer>
</main>
</body>
</html>
```